Calm and Compass Health Flyer (new business startup)

One page...clear enough to be read if faxed. This mental health clinic treats depression/anxiety in kids and adults. It also treats opiate and alcohol addiction. It's in downtown Elmira, NY and the owner of the clinic is from Elmira NY, where it's located. This clinic does not take health insurance, so it charges a low rate of $75 a visit once they pay the $125 starting fee.

Target Market(s)

doctors offices, new patients

Industry/Entity Type

Doctor

Requirements
Must have
• see microsoft word document. pdf is printed on the company letterhead.
Nice to have
• a simplified map would be nice. if you can include the building it would be a plus. The same two fonts were used in the business cards and letter head (kennedy small caps boo*) and Refrigerator Delux.

```html
<!DOCTYPE html>
<html lang="en">
<head>
<meta charset="utf-8">
<title>Calm and Compass Health Flyer</title>
<link rel="stylesheet" href="https://fonts.googleapis.com/css2?family=Cinzel:wght@500&family=Cormorant+SC:wght@600;700&family=Arimo:wght@700&display=swap">
<style>
  :root {
    --backdrop-top: #ffa21f;
    --backdrop-bottom: #ff6a12;
    --paper: #ffffff;
    --panel: #dcedf1;
    --ink: #141c3e;
    --brand-blue: #45c3ea;
    --brand-orange: #f05a28;
    --photo-light: #c9dde6;
    --photo-dark: #4a5f77;
    --map-base: #eef1f3;
    --building-brick: #8a4a36;
    --building-sky: #a9c6e4;
  }
  * { margin: 0; padding: 0; box-sizing: border-box; }
  html, body { width: 1200px; height: 1200px; overflow: hidden; }
  body {
    background: linear-gradient(180deg, var(--backdrop-top), var(--backdrop-bottom));
    position: relative;
    font-family: "Cormorant SC", Georgia, serif;
    color: var(--ink);
  }
  .flyer {
    position: absolute; left: 154px; top: 32px;
    width: 848px; height: 1130px;
    background: var(--panel);
    overflow: hidden;
  }
  .letterhead-curve { position: absolute; left: 0; top: 0; width: 848px; height: 230px; }
  .brand {
    position: absolute; left: 34px; top: 50px;
    display: flex; align-items: center; gap: 10px;
    font-family: "Arimo", Arial, sans-serif; font-weight: 700;
    font-size: 20px; color: var(--brand-orange);
  }
  .brand-dot { width: 30px; height: 30px; border-radius: 50%; background: var(--brand-orange); }
  .practice-name {
    position: absolute; left: 0; width: 848px; top: 78px;
    text-align: center; font-family: "Cinzel", "Times New Roman", serif;
    font-weight: 500; font-size: 56px; line-height: 1.2; color: var(--brand-blue);
    white-space: nowrap;
  }
  .credentials {
    position: absolute; left: 0; width: 848px; top: 137px;
    text-align: center; font-size: 15px; color: var(--brand-blue); font-weight: 600;
    white-space: nowrap;
  }
  .line {
    position: absolute; left: 60px; width: 732px;
    font-weight: 700; font-size: 40px; line-height: 1; white-space: nowrap;
  }
  .price-row { display: flex; align-items: baseline; }
  .leader { flex: 1; border-bottom: 4px dotted var(--ink); margin: 0 4px 6px; }
  .underlined { text-decoration: underline; text-decoration-thickness: 2px; }
  .tagline {
    position: absolute; left: 55px; top: 690px;
    font-style: italic; font-size: 18px; font-weight: 700; line-height: 22px;
  }
  .footnote {
    position: absolute; left: 55px; top: 731px; width: 745px;
    font-size: 14px; font-weight: 700; line-height: 20px;
  }
  .photo {
    position: absolute; left: 0; top: 772px; width: 330px; height: 358px;
    background: linear-gradient(180deg, var(--photo-light) 0%, var(--photo-dark) 70%, #6b5a4a 100%);
    -webkit-mask-image: linear-gradient(90deg, #000 75%, transparent);
    mask-image: linear-gradient(90deg, #000 75%, transparent);
  }
  .locator { position: absolute; left: 300px; top: 780px; width: 480px; height: 200px; }
  .contact {
    position: absolute; top: 992px;
    font-style: italic; font-weight: 700; font-size: 19px; line-height: 22px;
    white-space: nowrap;
  }
  .contact.address { left: 378px; }
  .contact.details { left: 564px; }
</style>
</head>
<body>
<main class="flyer">
  <svg class="letterhead-curve" viewBox="0 0 848 230" aria-hidden="true">
    <path d="M0 0 H848 V112 Q424 304 0 112 Z" fill="var(--paper)"/>
  </svg>

  <div class="brand"><span class="brand-dot"></span>Calm and Compass Health</div>
  <h1 class="practice-name">DANIEL REYES, RPA, PLLC</h1>
  <p class="credentials">(607) 555-0142 . Psychiatric Physician Assistant (PA-C,PSY-CAQ) . danielreyes@example.com</p>

  <p class="line" style="top:214px">Hours: &nbsp;Monday and Saturdays 9-4pm</p>
  <p class="line" style="top:265px">Psychiatric Evaluation</p>
  <p class="line price-row" style="top:318px"><span>(45min)</span><span class="leader"></span><span>$125*</span></p>
  <p class="line" style="top:367px">Psychiatric Office Visit</p>
  <p class="line price-row" style="top:420px"><span>(15min)</span><span class="leader"></span><span>$75*</span></p>

  <p class="line" style="top:498px">Ages: &nbsp;6 years old and up</p>
  <p class="line" style="top:544px"><span class="underlined">Conditions Treated</span>: &nbsp;Depression,</p>
  <p class="line" style="top:590px">Anxiety, PTSD, ADHD, Addiction,</p>
  <p class="line" style="top:637px">Bipolar, Childhood Mood Disorders</p>

  <p class="tagline">“We work for you, not the insurance companies”</p>
  <p class="footnote">*Although we do not partner with any Health Insurance Companies at this time, a bill will be provided to you at the time of service for you to submit to your insurance company.</p>

  <div class="photo" role="img" aria-label="Photo of a distressed young man sitting against a wall hugging his knees"></div>

  <svg class="locator" viewBox="0 0 480 200">
    <g role="img" aria-label="Simplified downtown street map with the clinic location">
      <ellipse cx="124" cy="102" rx="112" ry="92" fill="var(--map-base)"/>
    </g>
    <g role="img" aria-label="Photo of the brick office building on the main street">
      <defs>
        <linearGradient id="building" x1="0" y1="0" x2="0" y2="1">
          <stop offset="0" stop-color="var(--building-sky)"/>
          <stop offset="0.3" stop-color="var(--building-brick)"/>
          <stop offset="1" stop-color="#5c3a30"/>
        </linearGradient>
      </defs>
      <ellipse cx="346" cy="92" rx="112" ry="90" fill="url(#building)"/>
    </g>
  </svg>

  <p class="contact address">240 N. Water #118<br>Alder Falls,NY 14907<br>(p)607-555-0142<br>(f)607-555-0187</p>
  <p class="contact details">$75 office visits<br>danielreyes@example.com<br>with Dr. Helen Marsh<br>www.calm-compass.com</p>
</main>
</body>
</html>
```